Banner Design for Websites

I am looking for a few various banner designs of the below size. I want them to look authentic, bold and catchy.
Width 939
Height 262
Wording:
WANTED: DRIVEN AND SUCCESSFUL INDIVIDUALS READY TO TAKE THEIR RESULTS TO THE NEXT LEVEL.

Make up to $5000 per sale
No cold calling
No experience required
No pressure selling
NOT MLM

Personal Empowerment. The Next Big Business Boom !

I make well in excess of 10k per month consistently. Marnie K

Some photos attached for use and also some others banners for various workding other than above.

```html
<!DOCTYPE html>
<html lang="en">
<head>
<meta charset="utf-8">
<title>Personal Empowerment Banner</title>
<link href="https://fonts.googleapis.com/css2?family=Arimo:ital,wght@0,400;0,700;1,700&display=swap" rel="stylesheet">
<style>
  :root {
    --red: #d2161b;
    --red-dark: #a80d10;
    --red-light: #e8282a;
    --violet: #7472ea;
    --violet-light: #8b89f0;
    --lavender: #b9b6f6;
    --blue: #1d2fe6;
    --button: #5b5ff0;
    --gold: #f6b800;
    --gold-dark: #e08a00;
    --white: #ffffff;
    --photo-warm: #8a6b55;
    --photo-dark: #3b2e2a;
  }
  html, body {
    margin: 0;
    padding: 0;
    width: 1200px;
    height: 335px;
    overflow: hidden;
    background: var(--white);
  }
  .banner {
    position: relative;
    width: 939px;
    height: 262px;
    transform: scale(1.2780, 1.2786);
    transform-origin: 0 0;
    overflow: hidden;
    font-family: "Arimo", Arial, sans-serif;
    color: var(--white);
  }
  .banner-shapes {
    position: absolute;
    inset: 0;
  }
  .headline {
    position: absolute;
    left: 15px;
    top: 6px;
    display: flex;
    align-items: center;
    gap: 24px;
  }
  .headline-wanted {
    font-size: 47px;
    font-weight: 400;
    color: var(--blue);
    letter-spacing: -0.5px;
    line-height: 1;
  }
  .headline-copy {
    font-size: 18.5px;
    font-weight: 700;
    line-height: 23px;
    letter-spacing: 0.1px;
  }
  .tagline {
    position: absolute;
    left: 45px;
    top: 87px;
    font-size: 16px;
    font-weight: 700;
  }
  .benefits {
    position: absolute;
    left: 208px;
    top: 125px;
    margin: 0;
    padding: 0;
    list-style: none;
    font-size: 16.5px;
    line-height: 21.5px;
  }
  .photo-frame {
    position: absolute;
    left: 447px;
    top: 68px;
    width: 178px;
    height: 178px;
    border-radius: 50%;
    background: linear-gradient(135deg, var(--gold), var(--gold-dark));
    padding: 3px;
    box-sizing: border-box;
  }
  .photo {
    width: 100%;
    height: 100%;
    border-radius: 50%;
    background: radial-gradient(circle at 50% 40%, var(--photo-warm), var(--photo-dark));
  }
  .testimonial {
    position: absolute;
    left: 712px;
    top: 102px;
    width: 190px;
    font-size: 16px;
    font-style: italic;
    font-weight: 700;
    line-height: 21px;
    margin: 0;
  }
  .testimonial-author {
    position: absolute;
    left: 845px;
    top: 181px;
    font-size: 16px;
    font-weight: 700;
  }
  .cta {
    position: absolute;
    left: 762px;
    top: 210px;
    width: 138px;
    height: 40px;
    background: var(--button);
    outline: 2px dashed var(--white);
    outline-offset: -4px;
    text-align: center;
    text-decoration: none;
    color: var(--white);
    box-sizing: border-box;
    padding-top: 5px;
  }
  .cta-main {
    display: block;
    font-size: 19px;
    font-weight: 700;
    line-height: 19px;
  }
  .cta-sub {
    display: block;
    font-size: 10px;
    font-weight: 700;
    line-height: 12px;
  }
</style>
</head>
<body>
<div class="banner">
  <svg class="banner-shapes" viewBox="0 0 939 262" width="939" height="262" aria-hidden="true">
    <defs>
      <linearGradient id="header-fill" x1="0" y1="0" x2="0" y2="1">
        <stop offset="0" stop-color="var(--red-light)"/>
        <stop offset="1" stop-color="var(--red-dark)"/>
      </linearGradient>
      <linearGradient id="body-fill" x1="0" y1="0" x2="0" y2="1">
        <stop offset="0" stop-color="var(--violet-light)"/>
        <stop offset="1" stop-color="var(--violet)"/>
      </linearGradient>
      <linearGradient id="swoosh-fill" x1="0" y1="0" x2="1" y2="1">
        <stop offset="0" stop-color="var(--red-light)"/>
        <stop offset="1" stop-color="var(--red-dark)"/>
      </linearGradient>
      <linearGradient id="tick-fill" x1="0" y1="0" x2="1" y2="1">
        <stop offset="0" stop-color="#ffe04a"/>
        <stop offset="1" stop-color="var(--gold-dark)"/>
      </linearGradient>
    </defs>
    <rect class="body-bg" width="939" height="262" fill="url(#body-fill)"/>
    <rect class="header-underlay" y="50" width="939" height="30" fill="var(--lavender)"/>
    <path class="header-band" d="M0 0 H939 V64 Q939 72 930 72 H18 Q2 72 0 60 Z" fill="url(#header-fill)"/>
    <path class="right-swoosh" d="M620 262 C660 180 720 120 939 74 V262 Z" fill="url(#swoosh-fill)"/>
    <path class="right-swoosh-edge" d="M620 262 C660 180 720 120 939 74" fill="none" stroke="var(--gold)" stroke-width="2" opacity="0.6"/>
    <path class="bottom-wave" d="M0 228 C160 246 320 214 470 236 C540 246 580 250 620 262 H0 Z" fill="var(--red)"/>
    <path class="check-mark" d="M102 172 L128 160 L145 190 C165 160 185 140 198 132 L200 136 C178 160 160 186 146 214 L128 214 Z" fill="url(#tick-fill)"/>
    <text class="quote-open" x="702" y="118" font-family="Georgia, serif" font-size="56" fill="var(--white)">&#8220;</text>
    <text class="quote-close" x="890" y="176" font-family="Georgia, serif" font-size="56" fill="var(--white)">&#8221;</text>
  </svg>

  <div class="headline">
    <span class="headline-wanted">WANTED:</span>
    <span class="headline-copy">DRIVEN AND SUCCESSFUL INDIVIDUALS READY TO TAKE<br>THEIR RESULTS TO THE NEXT LEVEL</span>
  </div>

  <div class="tagline">Personal Empowerment. The Next Big Business Boom !</div>

  <ul class="benefits">
    <li>Make up to $5000 per sale</li>
    <li>No cold calling</li>
    <li>No experience required</li>
    <li>No pressure selling</li>
    <li>NOT MLM</li>
  </ul>

  <div class="photo-frame">
    <div class="photo" role="img" aria-label="Photo of two smiling business event attendees wearing lanyards"></div>
  </div>

  <p class="testimonial">I make well in excess of 10k per month consistently.</p>
  <div class="testimonial-author">Marnie K</div>

  <a class="cta" href="#">
    <span class="cta-main">CLICK HERE</span>
    <span class="cta-sub">FOR FREE INFO</span>
  </a>
</div>
</body>
</html>
```